All Natural Raw Honey & Goats Milk Body Wash Labels

We have launched a new product line of all natural Raw Honey & Goats Milk body wash with the business name being Vale Orin and the tag line Kindred . Their are currently three line items requiring three labels. Natural (Unscented), Japanese Honeysuckle and Caribbean.
It is a family orientated product that we want to promote as being all natural, healthy and trustworthy. It is an all Australian made product that uses our very own award winning raw honey
I can supply the file for the business name/logo upon request

Families

Bath & body

• a Lux high end feel
• simple easy to read with minimal images
• No cartoons

```html
<!DOCTYPE html>
<html lang="en">
<head>
<meta charset="utf-8">
<title>Vale Orin — Caribbean Body Wash Label</title>
<link rel="stylesheet" href="https://fonts.googleapis.com/css2?family=Cormorant+Garamond:wght@300;400&family=Arimo:wght@700&display=swap">
<style>
  :root {
    --page: #f4f5f5;
    --label: #e4f0ee;
    --label-edge: #b4c7c7;
    --comb-tone: #edf4f3;
    --heading-grey: #7d8182;
    --title-aqua: #a6c4c3;
    --mark-grey: #6f7374;
  }
  html, body {
    margin: 0;
    width: 1053px;
    height: 1200px;
    overflow: hidden;
    background: var(--page);
  }
  .label {
    position: absolute;
    left: 76px;
    top: 233px;
    width: 900px;
    height: 734px;
    background: var(--label);
    border-top: 6px solid var(--label-edge);
    border-bottom: 6px solid var(--label-edge);
    box-sizing: border-box;
    text-align: center;
  }
  .label__texture {
    position: absolute;
    left: 0;
    top: 0;
    width: 100%;
    height: 230px;
    background: linear-gradient(to bottom, var(--comb-tone), rgba(237, 244, 243, 0));
  }
  .label__product-line {
    position: absolute;
    left: 0;
    right: 0;
    top: 100px;
    margin: 0;
    font-family: "Arimo", Arial, sans-serif;
    font-weight: 700;
    font-size: 23px;
    letter-spacing: 0.2px;
    color: var(--heading-grey);
  }
  .label__scent {
    position: absolute;
    left: 0;
    right: 0;
    top: 255px;
    margin: 0;
    font-family: "Cormorant Garamond", serif;
    font-weight: 300;
    font-size: 122px;
    line-height: 1;
    letter-spacing: 1px;
    color: var(--title-aqua);
  }
  .brand {
    position: absolute;
    left: 0;
    right: 0;
    top: 480px;
    font-family: "Cormorant Garamond", serif;
    font-weight: 400;
    color: var(--mark-grey);
  }
  .brand__name {
    display: block;
    font-size: 48px;
    line-height: 1;
  }
  .brand__tagline {
    display: block;
    margin-top: 10px;
    font-size: 17px;
    letter-spacing: 9px;
    text-transform: uppercase;
  }
</style>
</head>
<body>
  <section class="label">
    <div class="label__texture" role="img" aria-label="Faint honeycomb pattern across the top of the label"></div>
    <p class="label__product-line">NATURAL RAW HONEY &amp; GOATS MILK BODY WASH</p>
    <h1 class="label__scent">CARIBBEAN</h1>
    <div class="brand">
      <span class="brand__name">Vale Orin</span>
      <span class="brand__tagline">Kindred .</span>
    </div>
  </section>
</body>
</html>
```